Gewinnspielseite
Zielgruppe
Familen mit Kindern
Aufgabenstellung
Design für eine Gewinnspiel bei dem freier Eintritt für 1 Jahr in alle Freizeitparks in Deutschland verlost werden soll. Ablauf wäre das die Gewinnerfamilie uns den Eintrittsbeleg zusendet und wir diesen dann erstatten bis zu einer maximalen Höhe von 5.000 Euro.
Menüpunkte: Startseite, Teilnahmebedingungen, Preisdetails, Teilnehmen, Datenschutz.
Es soll eine Intro-Seite auf der der Preis groß heraus gestellt ist gestaltet werden mit den
entsprechenden Menüpunkten sowie eine Template-Seite in der wir dann alle notwendigen Inhalte einfügen können.
Gewinnspiel von uns finden Sie auf www.lostrommel-beispiel.de damit Sie sich ein Bild über die bisherigen Gewinnspiele machen können.
WICHTIG: Es soll nur die Eingangsseite und eine Template Seite erstellt werden. Die komplette Programmierung bzw. Füllung mit Inhalten wird von uns gemacht!

```html
<!DOCTYPE html>
<html lang="de">
<head>
<meta charset="utf-8">
<title>Freizeitlos.de – Gewinnspiel</title>
<link href="https://fonts.googleapis.com/css2?family=Exo+2:ital,wght@0,600;0,700;1,600;1,700;1,800&family=Arimo:wght@400;700&display=swap" rel="stylesheet">
<style>
  :root{
    --sky-top:#cfe0f2;
    --sky-bottom:#e9f1f9;
    --page:#f1f2f4;
    --frame:#e6edf6;
    --panel-blue:#5e8fd4;
    --panel-light:#ffffff;
    --nav-bg:#c3d9f2;
    --nav-text:#1d3f78;
    --navy:#14306a;
    --green:#5cc01c;
    --green-dark:#2f8f0c;
    --copy:#1e2c48;
    --orange:#f7941d;
    --orange-light:#ffb347;
    --footer:#7b7f86;
    --white:#ffffff;
  }
  *{box-sizing:border-box;margin:0;padding:0}
  html,body{width:1200px;height:1073px;overflow:hidden}
  body{
    position:relative;
    background:linear-gradient(to bottom,var(--sky-top) 0,var(--sky-bottom) 356px,var(--page) 357px,#fafafa 1073px);
    font-family:"Arimo",Arial,sans-serif;
  }
  .hero-family{
    position:absolute;left:657px;top:0;width:419px;height:224px;
    background:radial-gradient(ellipse at 55% 45%,#e8c7a8 0,#d9b79a 30%,#c9d8e8 75%,rgba(207,224,242,0) 100%);
  }
  .brand{
    position:absolute;left:24px;top:128px;display:flex;align-items:center;gap:14px;
  }
  .brand-dot{width:64px;height:64px;border-radius:50%;background:var(--green)}
  .brand-name{
    font-family:"Exo 2",sans-serif;font-weight:700;font-size:56px;color:var(--navy);letter-spacing:-1px;
  }
  .main-nav{
    position:absolute;left:353px;top:219px;width:753px;height:42px;
    background:linear-gradient(to bottom,#d9e8f8,var(--nav-bg));
    border-radius:14px 14px 0 0;
  }
  .main-nav a{
    position:absolute;top:9px;font-family:"Exo 2",sans-serif;font-style:italic;font-weight:700;
    font-size:19px;color:var(--nav-text);text-decoration:none;
  }
  .main-nav a.is-active{color:var(--white)}
  .stage{
    position:absolute;left:95px;top:256px;width:1037px;height:757px;
    background:var(--frame);border-radius:14px;box-shadow:0 2px 6px rgba(0,0,0,.12);
  }
  .stage-inner{
    position:absolute;left:11px;top:10px;width:1016px;height:737px;border-radius:10px;overflow:hidden;
    background:linear-gradient(100deg,var(--panel-light) 0,#eaf1fb 18%,#b5cdee 40%,var(--panel-blue) 62%,#4f83cc 100%);
  }
  .headline{position:absolute;left:56px;font-family:"Exo 2",sans-serif;font-style:italic;white-space:nowrap}
  .headline-win{top:40px;font-size:40px;font-weight:800;color:var(--green)}
  .headline-prize{
    top:88px;left:70px;font-size:43px;font-weight:800;color:var(--white);
    -webkit-text-stroke:1.5px var(--navy);text-shadow:2px 2px 0 var(--navy);
  }
  .headline-parks{top:142px;left:124px;font-size:27px;font-weight:700;color:var(--navy)}
  .thumb{
    position:absolute;width:167px;height:166px;background:var(--white);border-radius:14px;padding:7px;
    box-shadow:0 1px 4px rgba(0,0,0,.2);
  }
  .thumb span{display:block;width:100%;height:100%;border-radius:9px}
  .thumb-water{left:630px;top:29px;width:162px}
  .thumb-water span{background:linear-gradient(to bottom,#4f8a86,#9fbfbc 55%,#eef3f4)}
  .thumb-coaster{left:820px;top:29px}
  .thumb-coaster span{background:linear-gradient(135deg,#3d7fd1,#8db6e6 50%,#2a3140)}
  .thumb-show{left:820px;top:220px}
  .thumb-show span{background:radial-gradient(circle at 50% 40%,#d7e6ff,#3566c9 45%,#101f62)}
  .divider{position:absolute;border-top:1px dotted rgba(255,255,255,.9)}
  .content{position:absolute;left:123px;top:238px;width:400px}
  .content h2{font-size:16px;font-weight:700;color:var(--navy);padding-bottom:6px;border-bottom:1px dotted rgba(255,255,255,.9);margin-bottom:13px}
  .content h2.light{color:var(--white)}
  .content p{font-size:12.5px;line-height:15.5px;color:var(--copy);text-align:justify;margin-bottom:15px}
  .content .block + .block{margin-top:33px}
  .cta{
    position:absolute;left:118px;top:611px;width:231px;height:48px;border-radius:10px;
    background:linear-gradient(to bottom,#8ee34a,var(--green) 50%,var(--green-dark));
    box-shadow:0 2px 4px rgba(0,0,0,.25);
    font-family:"Exo 2",sans-serif;font-style:italic;font-weight:800;font-size:27px;color:var(--white);
    text-align:center;line-height:46px;text-decoration:none;
  }
  .coaster-scene{
    position:absolute;left:530px;top:398px;width:440px;height:339px;
    background:radial-gradient(ellipse at 45% 70%,rgba(255,255,255,.75) 0,rgba(230,238,248,.45) 40%,rgba(94,143,212,0) 75%);
  }
  .ticket{position:absolute;left:894px;top:782px;width:266px;height:182px}
  .footer-links{
    position:absolute;left:928px;top:1027px;font-size:13px;color:var(--footer);letter-spacing:.3px;
  }
  .footer-links a{color:inherit;text-decoration:none}
  .footer-links span{margin:0 7px}
</style>
</head>
<body>
  <div class="hero-family" role="img" aria-label="Foto einer lächelnden Familie mit zwei Kindern"></div>

  <div class="brand">
    <span class="brand-dot"></span>
    <span class="brand-name">Freizeitlos.de</span>
  </div>

  <nav class="main-nav">
    <a class="is-active" style="left:24px">Startseite</a>
    <a style="left:129px">Teilnahmebedingungen</a>
    <a style="left:357px">Preisdetails</a>
    <a style="left:482px">Teilnehmen</a>
    <a style="left:605px">Datenschutz</a>
  </nav>

  <main class="stage">
    <div class="stage-inner">
      <div class="headline headline-win">Jetzt gewinnen:</div>
      <div class="headline headline-prize">freier Eintritt für 1 Jahr</div>
      <div class="headline headline-parks">in alle Freizeitparks in Deutschland</div>

      <div class="thumb thumb-water"><span role="img" aria-label="Foto einer Wildwasserbahn mit Gischt"></span></div>
      <div class="thumb thumb-coaster"><span role="img" aria-label="Foto einer Achterbahn mit Fahrgästen"></span></div>
      <div class="thumb thumb-show"><span role="img" aria-label="Foto einer Akrobatik-Show auf der Bühne"></span></div>

      <div class="coaster-scene" role="img" aria-label="Foto einer weißen Looping-Achterbahn vor blauem Himmel"></div>

      <div class="divider" style="left:131px;top:220px;width:343px"></div>

      <section class="content">
        <div class="block">
          <h2>Jetzt an der Verlosung teilnehmen</h2>
          <p>Einfach die Letzte Eintrittskarte vom Besuch einens Freizeitparks einsenden. Alle Einsendungen nehmen an der Verlosung teil.</p>
          <p>Einfach die Letzte Eintrittskarte vom Besuch einens Freizeitparks einsenden. Alle Einsendungen nehmen an der Verlosung teil.</p>
        </div>
        <div class="block">
          <h2 class="light">So geht's - schnell und einfach</h2>
          <p>Einfach die Letzte Eintrittskarte vom Besuch einens Freizeitparks einsenden. Alle Einsendungen nehmen an der Verlosung teil.</p>
          <p>Einfach die Letzte Eintrittskarte vom Besuch einens Freizeitparks einsenden. Alle Einsendungen nehmen an der Verlosung teil.einsenden. Alle Einsendungen nehmen an der Verlosung teil.</p>
        </div>
      </section>

      <a class="cta" href="#">mehr infos</a>
    </div>
  </main>

  <svg class="ticket" viewBox="0 0 266 182" aria-label="5.0000 Euro Gesamtwert">
    <g transform="rotate(-14 133 91)">
      <path d="M22 38 H244 V70 a14 14 0 0 0 0 28 V144 H22 V98 a14 14 0 0 0 0 -28 Z" fill="var(--orange)" stroke="#e07b0a" stroke-width="2"/>
      <path d="M34 48 H232 V134 H34 Z" fill="none" stroke="var(--orange-light)" stroke-width="2" stroke-dasharray="4 3"/>
      <text x="133" y="72" text-anchor="middle" font-size="22" fill="var(--orange-light)">★★★★★</text>
      <text x="133" y="100" text-anchor="middle" font-family="'Exo 2',sans-serif" font-weight="800" font-size="25" fill="#fff">5.0000 EURO</text>
      <text x="133" y="127" text-anchor="middle" font-family="'Exo 2',sans-serif" font-weight="800" font-size="25" fill="#fff">GESAMTWERT</text>
    </g>
  </svg>

  <footer class="footer-links"><a href="#">IMPRESSUM</a><span>|</span><a href="#">DATENSCHUTZ</a></footer>
</body>
</html>
```